BARRIER BANNER KTV

I am looking for a visual for a banner
3 meters long by 1 high.
In the same theme as the visual identity of the company.
As simple as possible without overloading

There must be the LOGO, the title VOLTARIS SERVICES TECHNIQUES

_________________________

I am looking for a visual for a banner (barrier banner)
3 meters long by 1 high.

AIR CONDITIONING HEATING VENTILATION
04 52 31 69 14

Font styles to use
Sans Serif

Colors
33b8a4
00a990
33a6d7
0493ce
3176b5
0355a3
ffffff

Requirements
Should not have
• No photo
No photo

```html
<!DOCTYPE html>
<html lang="fr">
<head>
<meta charset="utf-8">
<title>KTV – Barrier Banner</title>
<link rel="stylesheet" href="https://fonts.googleapis.com/css2?family=Arimo:wght@400;700&display=swap">
<style>
  :root {
    --navy-deep: #0e1421;
    --navy-mid: #1f2432;
    --navy-light: #2b303b;
    --accent-green: #3dbd8f;
    --accent-teal: #33b8a4;
    --accent-blue: #2a92c6;
    --white: #ffffff;
    --ink: #3b3b3d;
  }
  html, body {
    margin: 0;
    padding: 0;
    overflow: hidden;
    background: var(--white);
  }
  .banner {
    position: relative;
    width: 1200px;
    height: 400px;
    overflow: hidden;
    background: var(--white);
    font-family: "Arimo", Arial, sans-serif;
  }
  .banner__shapes {
    position: absolute;
    inset: 0;
  }
  .brand {
    position: absolute;
    left: 72px;
    top: 44px;
    display: flex;
    align-items: center;
    gap: 14px;
  }
  .brand__square {
    width: 22px;
    height: 22px;
    background: var(--accent-teal);
  }
  .brand__name {
    color: var(--white);
    font-weight: 700;
    font-size: 112px;
    line-height: 1;
    letter-spacing: 2px;
  }
  .company-name {
    position: absolute;
    left: 72px;
    top: 190px;
    margin: 0;
    color: var(--white);
    font-weight: 700;
    font-size: 49px;
    line-height: 59px;
    letter-spacing: 0.5px;
  }
  .phone {
    position: absolute;
    right: 48px;
    top: 42px;
    display: flex;
    align-items: center;
    gap: 10px;
    color: var(--ink);
    font-weight: 700;
    font-size: 41px;
    line-height: 1;
    letter-spacing: 0.5px;
  }
  .phone__icon {
    width: 32px;
    height: 32px;
  }
  .services {
    position: absolute;
    right: 48px;
    top: 272px;
    margin: 0;
    text-align: right;
    color: var(--ink);
    font-weight: 400;
    font-size: 47px;
    line-height: 47px;
  }
</style>
</head>
<body>
  <main class="banner">
    <svg class="banner__shapes" width="1200" height="400" viewBox="0 0 1200 400" aria-hidden="true">
      <defs>
        <linearGradient id="panel-fill" x1="0" y1="1" x2="1" y2="0">
          <stop offset="0" stop-color="var(--navy-deep)"/>
          <stop offset="0.6" stop-color="var(--navy-mid)"/>
          <stop offset="1" stop-color="var(--navy-light)"/>
        </linearGradient>
        <linearGradient id="stripe-fill" x1="0" y1="0" x2="1" y2="0">
          <stop offset="0" stop-color="var(--accent-green)"/>
          <stop offset="0.5" stop-color="var(--accent-teal)"/>
          <stop offset="1" stop-color="var(--accent-blue)"/>
        </linearGradient>
      </defs>
      <polygon class="dark-panel" points="0,0 825,0 559,400 0,400" fill="url(#panel-fill)"/>
      <polygon class="accent-stripe" points="701,90 765,90 559,400 490,400" fill="url(#stripe-fill)"/>
    </svg>

    <div class="brand">
      <span class="brand__name">KTV</span>
      <span class="brand__square"></span>
    </div>

    <h1 class="company-name">VOLTARIS<br>SERVICES<br>TECHNIQUES</h1>

    <div class="phone">
      <svg class="phone__icon" viewBox="0 0 24 24" fill="none" stroke="var(--ink)" stroke-width="2" stroke-linecap="round" stroke-linejoin="round" aria-hidden="true">
        <path d="M22 16.9v3a2 2 0 0 1-2.2 2 19.8 19.8 0 0 1-8.6-3.1 19.5 19.5 0 0 1-6-6A19.8 19.8 0 0 1 2.1 4.2 2 2 0 0 1 4.1 2h3a2 2 0 0 1 2 1.7c.1 1 .4 1.9.7 2.8a2 2 0 0 1-.5 2.1L8 9.9a16 16 0 0 0 6 6l1.3-1.3a2 2 0 0 1 2.1-.4c.9.3 1.8.6 2.8.7a2 2 0 0 1 1.7 2z"/>
        <path d="M14.5 2a8 8 0 0 1 7.5 7.5"/>
        <path d="M14.5 6a4 4 0 0 1 3.5 3.5"/>
      </svg>
      <span class="phone__number">04 52 31 69 14</span>
    </div>

    <p class="services">AIR CONDITIONING<br>HEATING VENTILATION</p>
  </main>
</body>
</html>
```